Startup Consultancy - Brochure Design

This needs to be a digital and potential hardcopy of a glossy brochure, designed to really catch the eye of prospective clients and draw them in. I am looking for something alternative from the "usual", but equally in keeping with the IT industry that the business operate in. The business specifically focuses on Print & Document Software and Technology solutions, and this should be considered in the design.

Target Market(s)

SMB and Corporate End Users, + Technology Resellers

Industry/Entity Type

Information Technology

Other font styles liked:
• Avenir

Colors
9d9d9d
848484
c3c3c3
e8e8e8
ffffff
eaeaea
0255a3
3176b5
85acd3

Requirements
Must have
• Company logo displayed on the front, plus any other relevant placements in pages
• Must follow the colour/style in some way of the website (www.brantwellconsultancy.co.uk)
Nice to have
• Some kind of infographical style in the brochure would be good, perhaps around the service listings

```html
<!DOCTYPE html>
<html lang="en">
<head>
<meta charset="utf-8">
<title>Brantwell – Brochure Front and Back</title>
<link href="https://fonts.googleapis.com/css2?family=Lato:wght@400;700&family=Michroma&display=swap" rel="stylesheet">
<style>
  :root {
    --stage: #959595;
    --page-dark: #0e0c0c;
    --page-black: #000000;
    --ink-light: #ffffff;
    --grass-deep: #0b1a05;
    --grass-mid: #2f6a12;
    --grass-bright: #7fc236;
    --bokeh-blue: #1c3fb0;
    --bokeh-green: #2c7a2a;
    --bokeh-yellow: #c9c23a;
    --bokeh-orange: #f0a020;
    --bokeh-red: #e0202f;
    --bokeh-magenta: #c01a7a;
  }
  * { margin: 0; padding: 0; box-sizing: border-box; }
  html, body { width: 1200px; height: 1200px; overflow: hidden; }
  body {
    position: relative;
    background: var(--stage);
    font-family: "Lato", Arial, sans-serif;
    color: var(--ink-light);
  }
  .page {
    position: absolute;
    width: 520px;
    height: 736px;
    overflow: hidden;
    box-shadow: 0 0 18px rgba(0,0,0,0.25);
  }
  .page--front { left: 54px; top: 227px; background: var(--page-dark); }
  .page--back { left: 617px; top: 225px; background: var(--page-black); border-left: 14px solid var(--page-black); }

  .brand-name {
    position: absolute;
    left: 0; right: 0;
    z-index: 2;
    text-align: center;
    font-family: "Lato", Arial, sans-serif;
    font-weight: 700;
    font-size: 38px;
    letter-spacing: 0.5px;
    color: var(--ink-light);
  }
  .page--front .brand-name { top: 144px; }
  .page--back .brand-name { top: 302px; }

  .welcome {
    position: absolute;
    top: 214px; left: 0; right: 0;
    text-align: center;
    font-family: "Michroma", "Arial", sans-serif;
    font-weight: 400;
    font-size: 41px;
    line-height: 1;
    letter-spacing: 1px;
  }
  .welcome-sub {
    position: absolute;
    top: 259px; left: 0; right: 0;
    text-align: center;
    font-family: "Michroma", "Arial", sans-serif;
    font-size: 18px;
    letter-spacing: 1.5px;
    padding-left: 10px;
  }
  .intro {
    position: absolute;
    top: 296px; left: 20px; right: 20px;
    text-align: center;
    font-weight: 700;
    font-size: 18px;
    line-height: 23.5px;
  }
  .photo-grass {
    position: absolute;
    left: 0; right: 0; top: 439px; bottom: 0;
    background:
      linear-gradient(180deg, var(--page-dark) 0%, rgba(14,12,12,0.6) 10%, rgba(0,0,0,0) 35%, rgba(0,0,0,0) 70%, rgba(0,0,0,0.55) 100%),
      radial-gradient(ellipse 70% 45% at 50% 38%, var(--grass-bright) 0%, var(--grass-mid) 55%, var(--grass-deep) 100%);
  }

  .bokeh {
    position: absolute;
    left: 0; right: 0;
    z-index: 0;
    background:
      linear-gradient(90deg, var(--bokeh-blue) 0%, var(--bokeh-green) 22%, var(--bokeh-yellow) 45%, var(--bokeh-orange) 62%, var(--bokeh-red) 85%, var(--bokeh-magenta) 100%);
  }
  .bokeh::after {
    content: "";
    position: absolute;
    inset: 0;
  }
  .bokeh--top { top: 0; height: 200px; }
  .bokeh--top::after { background: linear-gradient(180deg, rgba(0,0,0,0.25) 0%, rgba(0,0,0,0.2) 45%, var(--page-black) 100%); }
  .bokeh--bottom { bottom: 0; height: 220px; }
  .bokeh--bottom::after { background: linear-gradient(0deg, rgba(0,0,0,0.2) 0%, rgba(0,0,0,0.2) 50%, var(--page-black) 100%); }

  .address {
    position: absolute;
    z-index: 2;
    top: 368px; left: 0; right: 0;
    text-align: center;
    font-weight: 700;
    font-size: 21px;
    line-height: 29px;
  }
  .contact-line {
    position: absolute;
    z-index: 2;
    display: flex;
    align-items: center;
  }
  .contact-line--phone { top: 437px; left: 75px; }
  .contact-line--email { top: 473px; left: 73px; }
  .phone-number {
    font-family: "Michroma", "Arial", sans-serif;
    font-size: 25px;
    letter-spacing: 2px;
    margin-left: 12px;
  }
  .email-address {
    font-weight: 700;
    font-size: 17px;
    margin-left: 9px;
  }

  .page-label {
    position: absolute;
    top: 988px;
    width: 300px;
    text-align: center;
    font-family: "Lato", Arial, sans-serif;
    font-size: 52px;
    color: var(--ink-light);
    text-shadow: 0 0 12px rgba(0,0,0,0.2);
  }
  .page-label--front { left: 162px; }
  .page-label--back { left: 715px; }
</style>
</head>
<body>
  <section class="page page--front">
    <div class="brand-name">Brantwell</div>
    <h1 class="welcome">WELCOME</h1>
    <p class="welcome-sub">TO A NEW APPROACH</p>
    <p class="intro">We have a range of services suitable for a range of<br>clients including End Users, Channel<br>Partners, OEM’s and Distributors.</p>
    <div class="photo-grass" role="img" aria-label="Close-up photograph of fresh green grass blades against a dark background"></div>
  </section>

  <section class="page page--back">
    <div class="bokeh bokeh--top" role="img" aria-label="Colourful blurred bokeh lights fading into black"></div>
    <div class="bokeh bokeh--bottom" role="img" aria-label="Colourful blurred bokeh lights rising out of black"></div>
    <div class="brand-name">Brantwell</div>
    <p class="address">18-22 Carrow Lane,<br>London,EC1N 4PX</p>
    <div class="contact-line contact-line--phone">
      <svg width="22" height="22" viewBox="0 0 26 26" aria-hidden="true">
        <rect x="1" y="1" width="24" height="24" rx="5" fill="#ffffff"/>
        <path d="M9 6c-1.5 1-2 3-1 6 1 3 3 6 6 7.5 1.5.7 3 .5 4-.5l-2.2-2.6-1.8 1c-1.5-.8-3-3-3.5-4.8l1.6-1.2L10.8 6.2z" fill="#000000"/>
      </svg>
      <span class="phone-number">0203 555 0174</span>
    </div>
    <div class="contact-line contact-line--email">
      <svg width="26" height="15" viewBox="0 0 30 18" aria-hidden="true">
        <rect x="1" y="1" width="28" height="16" fill="#ffffff"/>
        <path d="M1 1 L15 11 L29 1 M1 17 L11 8 M29 17 L19 8" stroke="#000000" stroke-width="1.6" fill="none"/>
      </svg>
      <span class="email-address">enquiries@brantwellconsultancy.co.uk</span>
    </div>
  </section>

  <div class="page-label page-label--front">Front</div>
  <div class="page-label page-label--back">Back</div>
</body>
</html>
```